Design a Dynamic and User-Friendly Website for kLobbyra: Revolutionize Visitor Management

Description of kLobbyra:

kLobbyra is an innovative online visitor management system designed to streamline the process of managing visitors in various organizational settings. Our system automates the check-in process, enhances security by keeping accurate visitor logs, and ensures compliance with local regulations through customizable features. With functionalities such as contactless sign-in, real-time notifications, visitor badge printing, and comprehensive reporting, kLobbyra provides a modern solution to traditional visitor management challenges.

Target Audience:

Our primary target audience includes businesses and institutions across Africa, starting with Nigeria. This includes corporate offices, educational institutions, healthcare facilities, and government buildings that are looking for efficient, secure, and scalable visitor management solutions. Our system is particularly tailored to meet the needs of facility managers, security personnel, and front desk staff who prioritize ease of use, data security, and operational efficiency. Additionally, kLobbyra aims to cater to IT managers looking for robust systems that can seamlessly integrate with existing organizational infrastructure.

Color Scheme:

While specific colors are not mandated, the chosen palette should convey trust and stability, growth and efficiency, and maintain a professional and clean appearance. The colors selected should harmonize to create a welcoming, secure, and efficient atmosphere.
Typography:

Use modern, sans-serif fonts for readability and a contemporary look. Primary text should be clear with high contrast against the background, and headings can be bold to create a hierarchical structure that is easy to navigate.
Imagery:

Photography: High-quality images that feature African professionals and contexts, illustrating diverse, professional scenarios relevant to our target industries (such as corporate offices, educational institutions, healthcare facilities). Photos should authentically represent the African demographic, showing interactions between people and technology, emphasizing the ease and security of the visitor management process.
Illustrations: Custom illustrations that should culturally resonate with African settings and characters, vividly depicting functionalities of kLobbyra such as scanning a QR code, receiving a visitor badge, or receiving alerts on a smartphone or desktop. These illustrations should adopt a style that complements the overall design aesthetic of the site.
Layout and Design Elements:

A clean, minimalistic layout that focuses on usability with easy navigation paths for all user types.
Use cards or tiles for different sections such as features, testimonials, or case studies, which can help organize information cleanly and attractively.
Consider interactive elements like hover effects, animated transitions for loading elements, and subtle animations in illustrations to make the user experience dynamic and engaging.
Overall Theme:

The theme should be professional and welcoming, reflecting a high-tech solution that is approachable for users with varying levels of tech expertise. The design should instill confidence in the security and efficiency of the system, while also being culturally appropriate and user-friendly to encourage interaction and exploration of the site’s content.
This style and theme guide emphasizes flexibility in color usage while maintaining clear directives on the emotional and functional responses the design should invoke, ensuring it aligns with the values and needs of kLobbyra's target audience.

What websites can designers draw inspiration from?
List websites you like and describe what you like about them.

https://tallodesk.com/en-usremove
same industry so you can see their approaches to marketing to similar customers - granted their target is not specific to african market Very clean design and straight to the point. Their feature set is closest to our feature set.
http://www.gatrumo.comremove
clean design and straight to the point
http://vennatrak.comremove

Home Page
-------------------
Main Goal: Encourage visitors to start their 15-day free trial, effectively converting them into leads or potential customers.

Content Layout:
Hero Section: Engaging hero image or video that shows the kLobbyra system in action, with clear, prominent call-to-action (CTA) buttons for "Start your 15 day free trial" and secondary CTA for "Buy now"

Product Overview: Quick introduction to what kLobbyra is and its key benefits, such as enhanced security, easy integration, and improved operational efficiency.

Features Highlight: Brief visuals or icons depicting major features like contactless sign-in, real-time alerts, and comprehensive reporting.

How It Works: A concise step-by-step guide or graphic explaining how to get started with kLobbyra.

CTA Section: A more detailed call to action for starting the free trial,
if they want a more hands on guide allow them to schedule a demo and if they are ready click purchase to buy now.
Footer: Navigation links to other site sections, social media links, and legal information.

-------------------
Pricing Page
-------------------
Main Goal: Clearly convey the pricing structure in a way that users can easily understand and compare options based on their location and specific needs.

Content Layout:

Pricing Introduction: Explain the subscription model, highlighting the flexibility and scalability of the service (i.e., per location and additional tablets).

Country-Specific Pricing Tabs: Tabs or a dropdown menu allowing users to choose their country (Nigeria, Ghana, South Africa, Kenya) to view localized pricing in the respective currencies (NGN, GHS, ZAR, KES).
Subscription Per Location: Detailed pricing for managing a single location, with benefits listed beside the price

Tablets and Data Plans: A clear breakdown of the cost per tablet and the associated wireless data plans, including bulk discount options if applicable.
Interactive Pricing Calculator: A tool that allows users to calculate their monthly cost based on the number of locations and tablets they plan to use.

Add ons - for hardware, etc

FAQs: A section dedicated to frequently asked questions specifically about pricing, billing cycles, and cancellation policies.

CTA: Strong call to action for starting a free trial, with an emphasis on the ease of signing up and the no-commitment nature of the trial.

Footer: Standard navigational links, contact information, and social media buttons.

-------------------
Feature Page Template
-------------------
Main Goal: To detail individual features of kLobbyra, demonstrating the functionality and benefits to help prospective clients understand the value provided.

Content Layout:
Feature Introduction: Large title with a succinct description of the feature.

In-depth Details: Bullet points or short paragraphs explaining the feature, supported by relevant images or icons.

Use Case Scenario: Real-world application or a mini-case study showing the feature in action.

Benefit Summary: A list or graphic illustrating the benefits of the feature.

CTA: Prompt to try this feature via signup or schedule a demo speak with a sales representative.

Footer: Standard links and social media connections.

-------------------
Blog Page
-------------------
Main Goal: To engage current and prospective clients with useful content, position kLobbyra as a thought leader in the visitor management space, and improve SEO rankings.

Content Layout:
Featured Article: Highlight a recent or popular post prominently at the top.

Article List: Thumbnails and summaries of additional articles with clear categorization (e.g., Tips, Case Studies, Industry News).

Search and Filter Tools: Allow users to filter blog posts by topic, date, etc.

Newsletter Signup: Encourage visitors to subscribe to updates.
Social Share Buttons: Enable easy sharing of articles.
Footer: Include a comprehensive footer with navigational links and contact info.

Generic Content Page (e.g., Contact Us, About Us)
------------------------------
Main Goal: To provide essential information about the kLobbyra company or to facilitate contact with the company.

Content Layout:
Page Title and Introduction: Clear heading with a brief paragraph summarizing the page’s purpose.

Main Content Area: Detailed content appropriate to the page (e.g., company history, team bios for About Us; contact form, map, and helpline numbers for Contact Us).

Sidebar/Additional Elements: For Contact Us, include operational hours or a quick FAQ. For About Us, list awards or recognitions.

CTA: Depending on the page, direct users to other parts of the site (e.g., careers page link on About Us, newsletter sign-up on Contact Us).
Footer: Standard footer with expanded company details if on the Contact Us page.

Coding

```html
<!DOCTYPE html>
<html lang="en">
<head>
<meta charset="utf-8">
<title>kLobbyra – Visitor Management</title>
<link href="https://fonts.googleapis.com/css2?family=Lato:wght@400;700;900&family=DM+Sans:wght@400;500;700&display=swap" rel="stylesheet">
<style>
:root{
  --blue:#2b7bd3;
  --blue-dark:#1f66b8;
  --ink:#1d1d1f;
  --body:#3b3b3f;
  --muted:#5a5a60;
  --hero-bg:#e8f1fc;
  --soft-bg:#eaf2fc;
  --line:#d7e3f2;
  --white:#ffffff;
  --star:#f5a623;
  --footer-bar:#10243f;
  --cta-bg:#ecebe9;
  --client-ink:#3a3f47;
  --client-mark:#c4cedb;
}
*{box-sizing:border-box;margin:0;padding:0}
html,body{width:1200px;height:4216px;overflow:hidden}
body{font-family:'Lato',sans-serif;color:var(--body);background:var(--white);position:relative}
.abs{position:absolute}
section,header,footer{position:absolute;left:0;width:1200px}
.btn{position:absolute;display:flex;align-items:center;justify-content:center;font-family:'DM Sans',sans-serif;font-weight:500;font-size:12.5px;border-radius:5px;text-decoration:none}
.btn-solid{background:var(--blue);color:var(--white)}
.btn-outline{border:2px solid var(--blue);color:var(--ink);background:transparent}
.btn-pill{border-radius:20px}
.section-title{position:absolute;left:0;width:1200px;text-align:center;font-weight:700;font-size:44px;color:var(--ink)}
.title-rule{position:absolute;left:559px;width:82px;height:3px;background:var(--blue)}

/* header + hero */
.hero{top:0;height:704px;background:radial-gradient(ellipse at 75% 70%,#f3f8ff 0%,var(--hero-bg) 60%)}
.brand{display:flex;align-items:center;gap:8px;font-family:'DM Sans',sans-serif;font-size:34px;color:var(--ink);font-weight:400}
.brand-dot{width:30px;height:30px;border-radius:50%;border:4px solid var(--blue)}
.nav a{position:absolute;top:24px;font-family:'DM Sans',sans-serif;font-size:13px;color:var(--ink);text-decoration:none}
.nav a.active{color:var(--blue)}
.hero-title{position:absolute;left:142px;top:196px;font-size:31px;line-height:46px;font-weight:700;color:var(--ink);letter-spacing:.3px}
.hero-title .hl{color:var(--blue)}
.hero-list{position:absolute;left:142px;top:392px;list-style:none}
.hero-list li{display:flex;align-items:center;gap:8px;font-size:14px;color:var(--body);height:36px}
.hero-list svg{width:14px;height:14px}
.screens .screen{position:absolute;background:var(--white);border:2px solid #4a4f5a;border-radius:8px;box-shadow:0 6px 18px rgba(30,60,110,.12)}

/* about */
.about{top:704px;height:602px;background:var(--white)}
.about-art{position:absolute;left:131px;top:90px;width:426px;height:458px;border-radius:50%;background:radial-gradient(circle,#e9f1fb 0%,#f4f8fd 55%,#ffffff 72%)}
.about h2{position:absolute;left:640px;top:162px;font-size:33px;font-weight:700;color:var(--blue)}
.about p{position:absolute;left:640px;top:240px;width:412px;font-size:13.6px;line-height:22.6px;color:var(--body)}

/* features */
.features{top:1306px;height:712px;background:var(--soft-bg)}
.features-photo{position:absolute;left:142px;top:162px;width:436px;height:459px;border-radius:8px;background:linear-gradient(135deg,#b89a7c 0%,#d8d5d2 45%,#eef0f2 70%,#c9c2ba 100%)}
.feature-card{position:absolute;left:652px;width:365px;height:115px;background:var(--white);box-shadow:0 2px 10px rgba(40,80,140,.08)}
.feature-card h3{position:absolute;font-size:17px;font-weight:700;color:var(--ink)}
.feature-card p{position:absolute;font-size:12.3px;line-height:19.5px;color:var(--body);width:250px}
.icon-bubble{position:absolute;width:70px;height:70px;border-radius:50%;background:#f1f3f6;display:flex;align-items:center;justify-content:center}

/* how it works */
.how{top:2018px;height:591px;background:var(--white)}
.step{position:absolute;width:260px;text-align:center}
.step-ring{position:absolute;width:140px;height:140px;border-radius:50%;border:2px dashed #a9c7ec}
.step-core{position:absolute;left:14px;top:14px;width:108px;height:108px;border-radius:50%;background:var(--white);box-shadow:0 4px 14px rgba(40,80,140,.14);display:flex;align-items:center;justify-content:center}
.step-num{position:absolute;width:36px;height:36px;border-radius:50%;background:var(--blue);color:var(--white);font-weight:700;font-size:15px;display:flex;align-items:center;justify-content:center}
.step h3{position:absolute;left:0;width:260px;font-size:17px;font-weight:700;color:var(--ink)}
.step p{position:absolute;left:15px;width:230px;font-size:12.3px;line-height:19.5px;color:var(--body)}

/* cta band */
.cta{top:2609px;height:421px;background:var(--cta-bg)}
.cta-photo{position:absolute;left:589px;top:0;width:611px;height:421px;background:linear-gradient(90deg,#d9d6d2 0%,#e9e7e4 35%,#8a8f96 70%,#6f5a55 100%)}
.cta h2{position:absolute;left:143px;top:112px;width:460px;font-size:28px;line-height:38px;font-weight:700;color:#2d2d30}
.cta p{position:absolute;left:143px;top:205px;width:450px;font-size:13.4px;line-height:24px;color:var(--ink)}

/* testimonials */
.testimonials{top:3030px;height:510px;background:var(--white)}
.quote-card{position:absolute;top:179px;width:445px;height:167px;background:var(--white);box-shadow:0 3px 14px rgba(40,60,100,.1)}
.quote-card::after{content:"";position:absolute;left:68px;bottom:-16px;border-left:16px solid transparent;border-right:16px solid transparent;border-top:16px solid var(--white);filter:drop-shadow(0 3px 2px rgba(40,60,100,.06))}
.quote-mark{position:absolute;left:22px;top:8px;font-family:Georgia,serif;font-size:80px;line-height:80px;color:#d5e4f6;font-weight:700}
.quote-card p{position:absolute;left:30px;top:32px;width:395px;font-size:12.4px;line-height:21.7px;color:var(--body);text-indent:50px}
.person{position:absolute;top:388px;display:flex;align-items:center;gap:12px}
.avatar{width:56px;height:56px;border-radius:50%;background:linear-gradient(135deg,#6b4a3a,#c79b7e)}
.person h4{font-size:16px;font-weight:700;color:var(--blue)}
.stars{color:var(--star);font-size:13px;letter-spacing:2px}
.slider-arrow{position:absolute;width:36px;height:36px;border-radius:50%;background:var(--white);box-shadow:0 2px 8px rgba(40,60,100,.14);display:flex;align-items:center;justify-content:center;font-size:12px;color:#888}

/* clients */
.clients{top:3520px;height:322px;background:var(--white)}
.client-tile{position:absolute;top:135px;width:172px;height:91px;background:var(--white);box-shadow:0 3px 12px rgba(40,60,100,.09);display:flex;align-items:center;justify-content:center;gap:8px;font-size:24px;font-weight:700;color:var(--client-ink)}
.client-mark{width:18px;height:18px;border-radius:50%;background:var(--client-mark)}

/* footer */
.site-footer{top:3842px;height:324px;background:var(--blue)}
.site-footer .brand{color:var(--white);position:absolute;left:0;width:1200px;justify-content:center;top:72px;font-size:40px}
.site-footer .brand-dot{border-color:var(--white);width:34px;height:34px}
.footer-rule{position:absolute;left:142px;width:916px;height:1px;background:rgba(255,255,255,.35)}
.footer-nav a{position:absolute;top:180px;font-family:'DM Sans',sans-serif;font-size:13px;color:var(--white);text-decoration:none}
.contact{position:absolute;top:262px;display:flex;gap:12px;color:var(--white);font-size:12.5px;line-height:20px}
.contact-icon{width:28px;height:28px;border-radius:50%;background:var(--white);display:flex;align-items:center;justify-content:center;margin-top:4px}
.contact strong{font-weight:700}
.copyright{top:4166px;height:50px;background:var(--footer-bar);color:var(--white);font-size:13px;display:flex;align-items:center;justify-content:center}
</style>
</head>
<body>

<section class="hero">
  <header class="abs" style="top:0;left:0;width:1200px;height:70px">
    <div class="brand abs" style="left:141px;top:12px"><span class="brand-dot"></span>kLobbyra</div>
    <nav class="nav">
      <a class="active" style="left:421px" href="#">Home</a>
      <a style="left:485px" href="#">About</a>
      <a style="left:548px" href="#">Pricing</a>
      <a style="left:614px" href="#">Features</a>
      <a style="left:692px" href="#">Blog</a>
      <a style="left:747px" href="#">Contact Us</a>
    </nav>
    <a class="btn btn-solid" style="left:840px;top:15px;width:92px;height:36px">Log in</a>
    <a class="btn btn-outline" style="left:946px;top:15px;width:112px;height:38px">Free Trial</a>
  </header>

  <h1 class="hero-title"><span class="hl">EFFORTLESS ENTRY,</span><br><span class="hl">SEAMLESS SECURITY:</span><br>WELCOME TO THE FUTURE<br>OF <span class="hl">kLOBBYRA</span> MANAGEMENT.</h1>

  <ul class="hero-list">
    <li><svg viewBox="0 0 14 14"><circle cx="7" cy="7" r="6" fill="none" stroke="#2b7bd3" stroke-width="1.3"/><path d="M1 7h12M7 1c-2.5 3-2.5 9 0 12M7 1c2.5 3 2.5 9 0 12" fill="none" stroke="#2b7bd3" stroke-width="1"/></svg>Visitor management</li>
    <li><svg viewBox="0 0 14 14"><circle cx="7" cy="7" r="6" fill="none" stroke="#2b7bd3" stroke-width="1.3"/><path d="M1 7h12M7 1c-2.5 3-2.5 9 0 12M7 1c2.5 3 2.5 9 0 12" fill="none" stroke="#2b7bd3" stroke-width="1"/></svg>Staff and contractor sign in</li>
    <li><svg viewBox="0 0 14 14"><circle cx="7" cy="7" r="6" fill="none" stroke="#2b7bd3" stroke-width="1.3"/><path d="M1 7h12M7 1c-2.5 3-2.5 9 0 12M7 1c2.5 3 2.5 9 0 12" fill="none" stroke="#2b7bd3" stroke-width="1"/></svg>Desk and meeting room booking</li>
  </ul>

  <a class="btn btn-solid" style="left:141px;top:525px;width:213px;height:38px">Start Your 15 Day Free Trial</a>
  <a class="btn btn-outline" style="left:367px;top:525px;width:110px;height:39px">Buy Now</a>

  <div class="screens">
    <div class="screen" role="img" aria-label="kLobbyra settings dashboard screenshot" style="left:686px;top:213px;width:374px;height:260px"></div>
    <div class="screen" role="img" aria-label="kLobbyra visitor statistics screenshot" style="left:850px;top:237px;width:288px;height:116px"></div>
    <div class="screen" role="img" aria-label="kLobbyra account login screen" style="left:640px;top:381px;width:178px;height:176px"></div>
  </div>
</section>

<section class="about">
  <div class="about-art" role="img" aria-label="Illustration of a professional checking in at a digital visitor badge screen"></div>
  <h2>About kLobbyra</h2>
  <p>Lorem Ipsum is simply dummy text of the printing and typesetting industry. Lorem Ipsum has been the industry's standard dummy text ever since the 1500s, when an unknown printer took a galley of type and scrambled it to make a type specimen book. It has survived not only five centuries, but also the leap into electronic typesetting, remaining essentially unchanged. It was popularised in the 1960s with the release of Letraset sheets containing Lorem Ipsum passages, and more recently with desktop publishing software like Aldus PageMaker including versions of Lorem Ipsum.</p>
</section>

<section class="features">
  <h2 class="section-title" style="top:74px">Features</h2>
  <div class="title-rule" style="top:139px"></div>
  <div class="features-photo" role="img" aria-label="Photo of a visitor scanning a QR code on a reception tablet kiosk"></div>

  <div class="feature-card" style="top:167px">
    <div class="icon-bubble" style="left:20px;top:23px">
      <svg width="36" height="36" viewBox="0 0 36 36" fill="none" stroke="#333" stroke-width="1.6"><rect x="10" y="4" width="16" height="28" rx="3"/><path d="M15 8h6"/><rect x="14" y="13" width="8" height="8"/><path d="M17 26h2"/></svg>
    </div>
    <h3 style="left:96px;top:15px">Contactless Sign-in</h3>
    <p style="left:98px;top:39px">Lorem ipsum dolor sit amet, consectetur adipiscing elit, sed do eiusmod tempor esw incididunt ut labore et dolore</p>
  </div>

  <div class="feature-card" style="top:303px">
    <h3 style="left:26px;top:15px">Real-time Alerts</h3>
    <p style="left:28px;top:39px;width:220px">Lorem ipsum dolor sit amet lorem es consectetur adipiscing elit, sed do eiusmod tempor esw</p>
    <div class="icon-bubble" style="left:262px;top:20px">
      <svg width="36" height="36" viewBox="0 0 36 36" fill="none" stroke="#333" stroke-width="1.6"><rect x="5" y="9" width="26" height="20" rx="2"/><path d="M18 13l7 12H11z"/><path d="M18 17v4"/><path d="M9 5l2 3M27 5l-2 3M18 3v3"/></svg>
    </div>
  </div>

  <div class="feature-card" style="top:439px">
    <div class="icon-bubble" style="left:20px;top:23px">
      <svg width="36" height="36" viewBox="0 0 36 36" fill="none" stroke="#333" stroke-width="1.6"><rect x="8" y="5" width="22" height="27" rx="2"/><circle cx="14" cy="12" r="4"/><path d="M14 8v4h4"/><path d="M11 26l5-5 4 3 7-7"/><path d="M21 10h6M21 13h5"/></svg>
    </div>
    <h3 style="left:96px;top:15px">Comprehensive Reporting</h3>
    <p style="left:98px;top:39px">Lorem ipsum dolor sit amet, consectetur es adipiscing elit, sed do eiusmod tempor esw incididunt ut labore et dolore</p>
  </div>

  <a class="btn btn-solid btn-pill" style="left:651px;top:584px;width:203px;height:38px">Start Your 15 Day Free Trial</a>
</section>

<section class="how">
  <h2 class="section-title" style="top:80px">How It Works</h2>
  <div class="title-rule" style="top:146px"></div>

  <div class="step" style="left:163px;top:186px">
    <div class="step-ring" style="left:60px;top:0">
      <div class="step-core"><svg width="44" height="44" viewBox="0 0 44 44" fill="none" stroke="#333" stroke-width="1.6"><rect x="7" y="4" width="30" height="36" rx="3"/><circle cx="22" cy="15" r="5"/><path d="M14 27c2-5 14-5 16 0"/><path d="M12 32h20M12 35h20"/></svg></div>
    </div>
    <div class="step-num" style="left:60px;top:110px">1</div>
    <h3 style="top:162px">Lorem Ipsum Dolor</h3>
    <p style="top:192px">Lorem ipsum dolor sit consectetuer adipiscing elit, sed diam nonumy nibh euismod tincidunt ut.</p>
  </div>

  <svg class="abs" style="left:410px;top:236px" width="76" height="30" viewBox="0 0 76 30" fill="none" stroke="#9a9a9a" stroke-width="2"><path d="M4 22c18-14 44-16 66-4"/><path d="M62 12l8 6-9 4"/></svg>

  <div class="step" style="left:468px;top:186px">
    <div class="step-ring" style="left:60px;top:0">
      <div class="step-core"><svg width="44" height="44" viewBox="0 0 44 44" fill="none" stroke="#333" stroke-width="1.6"><path d="M22 24V6M22 6l-4 4M22 6l4 4M22 18l-9-7M13 11h5M13 11v5M22 18l9-7M31 11h-5M31 11v5"/><path d="M8 30c4-3 9-4 14-1l6 2c2 1 1 4-1 3l-6-1M8 36l6-1 12 3 12-8c1-2-1-3-3-2l-7 4"/></svg></div>
    </div>
    <div class="step-num" style="left:60px;top:110px">2</div>
    <h3 style="top:162px">Lorem Ipsum Dolor</h3>
    <p style="top:192px">Lorem ipsum dolor sit consectetuer adipiscing elit, sed diam nonumy nibh euismod tincidunt ut.</p>
  </div>

  <svg class="abs" style="left:716px;top:236px" width="76" height="30" viewBox="0 0 76 30" fill="none" stroke="#9a9a9a" stroke-width="2"><path d="M4 16c18 10 44 10 66-6"/><path d="M60 6l10 4-5 8"/></svg>

  <div class="step" style="left:774px;top:186px">
    <div class="step-ring" style="left:60px;top:0">
      <div class="step-core"><svg width="44" height="44" viewBox="0 0 44 44" fill="none" stroke="#333" stroke-width="1.6"><circle cx="14" cy="12" r="8"/><circle cx="30" cy="12" r="8"/><circle cx="14" cy="30" r="8"/><circle cx="30" cy="30" r="8"/><circle cx="14" cy="10" r="2.5"/><path d="M10 16c1-3 7-3 8 0"/><circle cx="30" cy="28" r="2.5"/><path d="M26 34c1-3 7-3 8 0"/></svg></div>
    </div>
    <div class="step-num" style="left:60px;top:110px">3</div>
    <h3 style="top:162px">Lorem Ipsum Dolor</h3>
    <p style="top:192px">Lorem ipsum dolor sit consectetuer adipiscing elit, sed diam nonumy nibh euismod tincidunt ut.</p>
  </div>

  <a class="btn btn-solid btn-pill" style="left:498px;top:462px;width:204px;height:38px">Start Your 15 Day Free Trial</a>
</section>

<section class="cta">
  <div class="cta-photo" role="img" aria-label="Photo of a professional signing in on a reception kiosk tablet"></div>
  <h2>Lorem Ipsum Dolor Sit Sed Diam Consectetuer Adipiscing</h2>
  <p>Lorem ipsum dolor sit amet, consectetur adipiscing elit, sed do eiusmod tempor incididunt</p>
  <a class="btn btn-solid btn-pill" style="left:143px;top:268px;width:203px;height:38px">Start Your 15 Day Free Trial</a>
</section>

<section class="testimonials">
  <h2 class="section-title" style="top:84px">Client Testimonials</h2>
  <div class="title-rule" style="top:146px"></div>
  <div class="slider-arrow" style="left:85px;top:255px">&#8249;</div>
  <div class="slider-arrow" style="left:1082px;top:255px">&#8250;</div>

  <div class="quote-card" style="left:144px">
    <span class="quote-mark">&#8220;</span>
    <p>Lorem ipsum amet, consectetuer adipisciggng elit, sed diam nonummy nibh euismod tincidunt ut laoreet doore magna aliqum erat volfgutpat. Ut wisi enim ad mifggnim veniam, quis nostrud exerci ese tation ullamcgorper suscipit lobotis nisl aliquip ex ea comhgmodo as consequat mifggnim veniam</p>
  </div>
  <div class="quote-card" style="left:617px">
    <span class="quote-mark">&#8220;</span>
    <p>Lorem ipsum amet, consectetuer adipisciggng elit, sed diam nonummy nibh euismod tincidunt ut laoreet doore magna aliqum erat volfgutpat. Ut wisi enim ad mifggnim veniam, quis nostrud exerci ese tation ullamcgorper suscipit lobotis nisl aliquip ex ea comhgmodo asa consequat mifggnim veniam</p>
  </div>

  <div class="person" style="left:145px">
    <div class="avatar" role="img" aria-label="Portrait photo of Tobi Adeyemi"></div>
    <div><h4>Tobi Adeyemi</h4><div class="stars">★★★★★</div></div>
  </div>
  <div class="person" style="left:613px">
    <div class="avatar" role="img" aria-label="Portrait photo of Amaka Obi"></div>
    <div><h4>Amaka Obi</h4><div class="stars">★★★★★</div></div>
  </div>
</section>

<section class="clients">
  <h2 class="section-title" style="top:34px">Our Clients</h2>
  <div class="title-rule" style="top:93px"></div>
  <div class="slider-arrow" style="left:85px;top:162px">&#8249;</div>
  <div class="slider-arrow" style="left:1082px;top:162px">&#8250;</div>
  <div class="client-tile" style="left:144px"><span class="client-mark"></span>Zenbori</div>
  <div class="client-tile" style="left:327px"><span class="client-mark"></span>Tulvane</div>
  <div class="client-tile" style="left:512px"><span class="client-mark"></span>Orimbe</div>
  <div class="client-tile" style="left:699px"><span class="client-mark"></span>Plexora</div>
  <div class="client-tile" style="left:887px"><span class="client-mark"></span>Maruvo</div>
</section>

<footer class="site-footer">
  <div class="brand"><span class="brand-dot"></span>kLobbyra</div>
  <div class="footer-rule" style="top:152px"></div>
  <nav class="footer-nav">
    <a style="left:208px" href="#">Home</a>
    <a style="left:346px" href="#">About Us</a>
    <a style="left:503px" href="#">Pricing</a>
    <a style="left:648px" href="#">Feature</a>
    <a style="left:797px" href="#">Blog</a>
    <a style="left:927px" href="#">Contact Us</a>
  </nav>
  <div class="footer-rule" style="top:231px"></div>
  <div class="contact" style="left:234px">
    <span class="contact-icon"><svg width="14" height="14" viewBox="0 0 14 14"><path d="M7 1a4 4 0 0 1 4 4c0 3-4 8-4 8S3 8 3 5a4 4 0 0 1 4-4z" fill="none" stroke="#2b7bd3" stroke-width="1.4"/><circle cx="7" cy="5" r="1.4" fill="#2b7bd3"/></svg></span>
    <div>123, Building Name, Street<br>City, State XY 123456</div>
  </div>
  <div class="contact" style="left:562px">
    <span class="contact-icon"><svg width="14" height="14" viewBox="0 0 14 14"><path d="M3 1.5l2 .2 1 3-1.5 1a7 7 0 0 0 3.8 3.8l1-1.5 3 1 .2 2c-.2 1-1 1.5-2 1.5A10 10 0 0 1 1.5 3.5c0-1 .5-1.8 1.5-2z" fill="none" stroke="#2b7bd3" stroke-width="1.3"/></svg></span>
    <div><strong>Phone</strong><br>123-456-7890</div>
  </div>
  <div class="contact" style="left:824px">
    <span class="contact-icon"><svg width="14" height="14" viewBox="0 0 14 14"><rect x="1.5" y="3" width="11" height="8" rx="1" fill="none" stroke="#2b7bd3" stroke-width="1.3"/><path d="M1.5 3.5L7 8l5.5-4.5" fill="none" stroke="#2b7bd3" stroke-width="1.3"/></svg></span>
    <div><strong>Email</strong><br>info@klobbyra.com</div>
  </div>
</footer>
<div class="copyright abs" style="left:0;width:1200px">© 2024 kLobbyra. All Rights Reserved.</div>

</body>
</html>
```